Falcrest security business card

Looking for a business card for my security company

Target Market(s)

Security

Industry/Entity Type

Security

Contact Information for Business Card

Name - Gil Marston. Title - General manager - direct 314 862.4490 website www. falcrestsecurityservices.example email - gil@ falcrestsecurityservices.example

Requirements
Must have
• Logo attached

```html
<!DOCTYPE html>
<html lang="en">
<head>
<meta charset="utf-8">
<title>Falcrest Security Services – Business Cards</title>
<link rel="stylesheet" href="https://fonts.googleapis.com/css2?family=Heebo:wght@400;500;700&display=swap">
<style>
  :root {
    --page: #262626;
    --ink: #121417;
    --ink-soft: #1c1f23;
    --gold: #c9a45c;
    --gold-light: #f1d88a;
    --gold-dark: #6e4e25;
    --cream: #efe6d9;
    --bronze: #7a5530;
    --text-dark: #1e1e1e;
    --text-light: #f3ead8;
  }
  * { margin: 0; padding: 0; box-sizing: border-box; }
  html, body { width: 736px; height: 1200px; overflow: hidden; background: var(--page); }
  body { position: relative; font-family: "Heebo", sans-serif; }

  .card {
    position: absolute;
    left: 88px;
    width: 561px;
    height: 309px;
    overflow: hidden;
    background: linear-gradient(135deg, var(--ink-soft), var(--ink));
  }
  .card--dark  { top: 88px; }
  .card--split { top: 441px; }
  .card--wave  { top: 795px; }
  .card__bg { position: absolute; inset: 0; width: 100%; height: 100%; }

  .brand {
    position: absolute;
    left: 138px; top: 170px;
    transform: translate(-50%, -50%);
    display: flex; align-items: center; gap: 10px;
  }
  .brand__mark { width: 14px; height: 14px; background: var(--gold); }
  .brand__name {
    font-weight: 700; font-size: 38px; letter-spacing: 1px;
    text-transform: uppercase; color: var(--gold);
  }

  .divider {
    position: absolute; left: 264px; top: 82px;
    width: 1px; height: 140px; background: var(--gold);
  }

  .contact { position: absolute; left: 294px; top: 74px; }
  .card--wave .contact { left: 299px; }
  .contact__name { font-size: 18px; font-weight: 400; line-height: 1.1; }
  .contact__title { font-size: 11.5px; margin-top: 1px; margin-left: 1px; }
  .contact__list { list-style: none; margin-top: 20px; }
  .contact__item {
    display: flex; align-items: center;
    height: 17px; margin-bottom: 19px;
    font-size: 12px;
  }
  .contact__icon { width: 34px; flex: none; }
  .contact__icon svg { display: block; }

  .card--dark .contact__name { color: var(--gold); }
  .card--dark .contact__title,
  .card--dark .contact__item { color: var(--text-light); }
  .card--split .contact__name,
  .card--split .contact__title,
  .card--split .contact__item { color: var(--text-dark); }
  .card--wave .contact__name,
  .card--wave .contact__title,
  .card--wave .contact__item { color: var(--text-light); }
</style>
</head>
<body>

<svg width="0" height="0" style="position:absolute">
  <defs>
    <linearGradient id="goldFlow" x1="0" y1="0" x2="1" y2="1">
      <stop offset="0" stop-color="#6e4e25"/>
      <stop offset="0.5" stop-color="#b89154"/>
      <stop offset="1" stop-color="#f1d88a"/>
    </linearGradient>
    <linearGradient id="goldFlowRev" x1="0" y1="1" x2="1" y2="0">
      <stop offset="0" stop-color="#7a5a2e"/>
      <stop offset="0.6" stop-color="#b18a4e"/>
      <stop offset="1" stop-color="#f3dc8e"/>
    </linearGradient>
    <linearGradient id="goldBar" x1="0" y1="0" x2="0" y2="1">
      <stop offset="0" stop-color="#8a6532"/>
      <stop offset="0.5" stop-color="#f1d88a"/>
      <stop offset="1" stop-color="#8a6532"/>
    </linearGradient>
    <linearGradient id="goldSweep" x1="0" y1="1" x2="1" y2="0">
      <stop offset="0" stop-color="#f5df8f"/>
      <stop offset="0.5" stop-color="#b38c4f"/>
      <stop offset="1" stop-color="#7a5530"/>
    </linearGradient>
  </defs>
</svg>

<!-- Card 1: all dark -->
<section class="card card--dark">
  <svg class="card__bg" viewBox="0 0 561 309" aria-hidden="true">
    <path d="M0 0 H210 C180 40 150 55 110 60 C60 66 20 85 0 116 Z" fill="url(#goldFlow)"/>
    <path d="M0 0 H140 C110 30 80 40 50 55 C25 68 8 80 0 95 Z" fill="#8c6a36" opacity="0.8"/>
    <path d="M348 309 C380 260 420 240 480 240 C530 238 552 215 561 185 V309 Z" fill="url(#goldFlowRev)"/>
    <path d="M412 309 C440 275 480 265 520 255 C545 248 556 235 561 225 V309 Z" fill="#8a6432" opacity="0.75"/>
  </svg>
  <div class="brand"><span class="brand__mark"></span><span class="brand__name">Falcrest</span></div>
  <div class="divider"></div>
  <div class="contact">
    <p class="contact__name">Gil Marston</p>
    <p class="contact__title">General manager</p>
    <ul class="contact__list">
      <li class="contact__item"><span class="contact__icon"><svg width="17" height="17" viewBox="0 0 24 24" fill="none" stroke="#c9a45c" stroke-width="1.5"><path d="M5 3h4l2 5-2.5 1.5a11 11 0 0 0 6 6L16 13l5 2v4a2 2 0 0 1-2 2A17 17 0 0 1 3 5a2 2 0 0 1 2-2z"/><path d="M14 3a7 7 0 0 1 7 7M14 7a3 3 0 0 1 3 3"/></svg></span>314 862.4490</li>
      <li class="contact__item"><span class="contact__icon"><svg width="20" height="14" viewBox="0 0 20 14" fill="none" stroke="#c9a45c" stroke-width="1.3"><rect x="0.7" y="0.7" width="18.6" height="12.6"/><path d="M0.7 0.7 10 8l9.3-7.3M0.7 13.3 7.5 6M19.3 13.3 12.5 6"/></svg></span>gil@falcrestsecurityservices.example</li>
      <li class="contact__item"><span class="contact__icon"><svg width="11" height="15" viewBox="0 0 11 15"><path d="M1 0v13l3-3 2.5 5 2-1-2.5-5H10z" fill="#c9a45c"/></svg></span>www.falcrestsecurityservices.example</li>
    </ul>
  </div>
</section>

<!-- Card 2: dark and cream split -->
<section class="card card--split">
  <svg class="card__bg" viewBox="0 0 561 309" aria-hidden="true">
    <rect x="264" y="0" width="297" height="309" fill="var(--cream)"/>
    <rect x="264" y="0" width="8" height="309" fill="url(#goldBar)"/>
    <path d="M0 0 H197 C170 35 140 45 100 52 C55 60 18 85 0 100 Z" fill="url(#goldFlow)"/>
    <path d="M0 0 H130 C100 28 72 38 45 50 C22 62 7 74 0 86 Z" fill="#8c6a36" opacity="0.8"/>
    <path d="M365 309 C395 270 430 255 485 250 C535 245 552 215 561 190 V309 Z" fill="url(#goldFlowRev)"/>
    <path d="M430 309 C455 285 490 275 525 265 C548 258 557 245 561 235 V309 Z" fill="#8a6432" opacity="0.75"/>
  </svg>
  <div class="brand"><span class="brand__mark"></span><span class="brand__name">Falcrest</span></div>
  <div class="contact">
    <p class="contact__name">Gil Marston</p>
    <p class="contact__title">General manager</p>
    <ul class="contact__list">
      <li class="contact__item"><span class="contact__icon"><svg width="17" height="17" viewBox="0 0 24 24" fill="none" stroke="#c9a45c" stroke-width="1.5"><path d="M5 3h4l2 5-2.5 1.5a11 11 0 0 0 6 6L16 13l5 2v4a2 2 0 0 1-2 2A17 17 0 0 1 3 5a2 2 0 0 1 2-2z"/><path d="M14 3a7 7 0 0 1 7 7M14 7a3 3 0 0 1 3 3"/></svg></span>314 862.4490</li>
      <li class="contact__item"><span class="contact__icon"><svg width="20" height="14" viewBox="0 0 20 14" fill="none" stroke="#b8914e" stroke-width="1.3"><rect x="0.7" y="0.7" width="18.6" height="12.6"/><path d="M0.7 0.7 10 8l9.3-7.3M0.7 13.3 7.5 6M19.3 13.3 12.5 6"/></svg></span>gil@falcrestsecurityservices.example</li>
      <li class="contact__item"><span class="contact__icon"><svg width="11" height="15" viewBox="0 0 11 15"><path d="M1 0v13l3-3 2.5 5 2-1-2.5-5H10z" fill="#b8914e"/></svg></span>www.falcrestsecurityservices.example</li>
    </ul>
  </div>
</section>

<!-- Card 3: dark with bronze sweep -->
<section class="card card--wave">
  <svg class="card__bg" viewBox="0 0 561 309" aria-hidden="true">
    <rect x="0" y="0" width="561" height="309" fill="var(--bronze)"/>
    <path d="M0 0 H325 C300 15 290 60 285 110 C280 160 255 200 210 215 C150 235 90 240 45 309 H0 Z" fill="var(--ink-soft)"/>
    <path d="M325 0 C300 15 290 60 285 110 C280 160 255 200 210 215 C150 235 90 240 45 309" fill="none" stroke="#e9cf85" stroke-width="3"/>
    <path d="M45 309 C90 240 150 235 210 220 C260 205 320 210 420 215 C500 220 545 200 561 185 V309 Z" fill="url(#goldSweep)" opacity="0.9"/>
    <path d="M450 309 C480 285 515 275 545 272 L561 270 V309 Z" fill="#231c19"/>
    <path d="M0 0 H197 C170 35 140 45 100 52 C55 60 18 85 0 100 Z" fill="url(#goldFlow)"/>
    <path d="M0 0 H130 C100 28 72 38 45 50 C22 62 7 74 0 86 Z" fill="#8c6a36" opacity="0.8"/>
  </svg>
  <div class="brand"><span class="brand__mark"></span><span class="brand__name">Falcrest</span></div>
  <div class="contact">
    <p class="contact__name">Gil Marston</p>
    <p class="contact__title">General manager</p>
    <ul class="contact__list">
      <li class="contact__item"><span class="contact__icon"><svg width="17" height="17" viewBox="0 0 24 24" fill="none" stroke="#d8bc7e" stroke-width="1.5"><path d="M5 3h4l2 5-2.5 1.5a11 11 0 0 0 6 6L16 13l5 2v4a2 2 0 0 1-2 2A17 17 0 0 1 3 5a2 2 0 0 1 2-2z"/><path d="M14 3a7 7 0 0 1 7 7M14 7a3 3 0 0 1 3 3"/></svg></span>314 862.4490</li>
      <li class="contact__item"><span class="contact__icon"><svg width="20" height="14" viewBox="0 0 20 14" fill="none" stroke="#d8bc7e" stroke-width="1.3"><rect x="0.7" y="0.7" width="18.6" height="12.6"/><path d="M0.7 0.7 10 8l9.3-7.3M0.7 13.3 7.5 6M19.3 13.3 12.5 6"/></svg></span>gil@falcrestsecurityservices.example</li>
      <li class="contact__item"><span class="contact__icon"><svg width="11" height="15" viewBox="0 0 11 15"><path d="M1 0v13l3-3 2.5 5 2-1-2.5-5H10z" fill="#d8bc7e"/></svg></span>www.falcrestsecurityservices.example</li>
    </ul>
  </div>
</section>

</body>
</html>
```